Marketing Advertisement

I would like to design a DL size flyer to promote our company to our Tradely customers. Our company name is Shuttle Forge. We are badminton equipment retail shop and online shop. This is a new company on the market. The most unique thing about company is we carried the most brands compare to our competitors including KESTRA(authorise retailer), Plume, Norvek (authorise retailer), Tavori and Ru-Pao. Hence we have more products compare to others. Furthermore we carries all range of products (Rackets,Shoes, Apparels, Bags, Accessories, Shuttlecocks)We offer shipping to Australia wide and New Zealand wide and free shipping when purchase over $150.00Ideally we want to promote use the Tradely channel to promote our website (www.rallyhaven.com.au) and our physical store. For our website we have a promo for first time purchase using the promo code "Hello18". For our physical store we are partner with KESTRA Badminton Centre as they are the venue provider. I would like the design to be in both horizontal or vertical.
Look and feel

```html
<!DOCTYPE html>
<html lang="en">
<head>
<meta charset="utf-8">
<title>Shuttle Forge – DL Flyer</title>
<link rel="stylesheet" href="https://fonts.googleapis.com/css2?family=Bebas+Neue&family=Lato:wght@400;700;900&display=swap">
<style>
  :root {
    --navy: #232a55;
    --coral: #ec5a4a;
    --cream: #f3f1e6;
    --white: #ffffff;
    --backdrop: #e4e2dc;
    --photo-deep: #2b2b6a;
    --photo-warm: #8a2a6a;
  }
  * { box-sizing: border-box; margin: 0; padding: 0; }
  html, body { width: 1200px; height: 858px; overflow: hidden; background: var(--backdrop); }
  .canvas { position: relative; width: 1200px; height: 858px; }
  .flyer {
    position: absolute; left: 410px; top: 29px; width: 380px; height: 800px;
    background: var(--cream); overflow: hidden;
    font-family: "Lato", sans-serif;
    box-shadow: 0 6px 24px rgba(0,0,0,.18);
  }
  .hero-photo {
    position: absolute; left: 0; top: 0; width: 380px; height: 340px;
    background: radial-gradient(circle at 65% 40%, #4a4fa0 0%, var(--photo-deep) 45%, var(--photo-warm) 100%);
  }
  .shapes { position: absolute; inset: 0; }
  .brand-mark {
    position: absolute; right: 22px; top: 238px;
    display: flex; align-items: center; gap: 8px;
    color: var(--white); font-weight: 900; font-size: 22px; line-height: 1;
  }
  .brand-mark .dot { width: 16px; height: 16px; border-radius: 50%; background: var(--coral); }
  .headline {
    position: absolute; left: 22px; top: 356px;
    font-family: "Bebas Neue", sans-serif; font-size: 50px; line-height: 1;
    color: var(--white); letter-spacing: .5px; white-space: nowrap; font-weight: 400;
  }
  .subline {
    position: absolute; left: 24px; top: 412px;
    font-size: 15px; font-weight: 700; color: var(--coral); white-space: nowrap;
  }
  .product-photo {
    position: absolute; border-radius: 50%; border: 4px solid var(--navy);
  }
  .product-photo.racket { left: 22px; top: 478px; width: 96px; height: 96px; background: radial-gradient(circle, #3a3f5a, #15182b); }
  .product-photo.bags { left: 112px; top: 452px; width: 150px; height: 150px; background: linear-gradient(160deg, #5bc0a0, #2e59b8 45%, #d8443c 75%, #1d2a6a); }
  .product-photo.shoes { left: 262px; top: 470px; width: 104px; height: 104px; background: linear-gradient(135deg, #2fb59a, #e8d64a); }
  .brand-list {
    position: absolute; left: 22px; top: 606px; width: 170px;
    display: flex; flex-wrap: wrap; gap: 6px 12px; list-style: none;
    font-size: 13px; font-weight: 900; color: var(--navy); text-transform: uppercase;
  }
  .shipping {
    position: absolute; right: 14px; top: 622px; width: 112px; text-align: right;
    font-size: 12px; line-height: 15px; color: var(--navy); font-weight: 700;
  }
  .shipping .free { color: var(--coral); }
  .shipping .price { display: block; font-size: 24px; line-height: 1.1; font-weight: 900; color: var(--coral); margin-top: 2px; }
  .promo { position: absolute; left: 20px; top: 668px; color: var(--coral); }
  .promo-rate { display: flex; align-items: center; gap: 8px; }
  .promo-rate .percent { font-size: 42px; font-weight: 900; line-height: 1; }
  .promo-rate .label { font-size: 12px; font-weight: 700; line-height: 1.1; text-transform: uppercase; }
  .promo-code-label { font-size: 10px; font-weight: 700; letter-spacing: 1px; margin-top: 6px; }
  .promo-code { font-size: 21px; font-weight: 700; color: var(--white); }
  .promo-ends { font-size: 10px; font-style: italic; }
  .website {
    position: absolute; right: 14px; bottom: 10px;
    font-size: 14px; font-weight: 700; color: var(--white);
  }
</style>
</head>
<body>
<div class="canvas">
  <article class="flyer">
    <div class="hero-photo" role="img" aria-label="Close-up photo of a player's hand serving a shuttlecock with a racket"></div>

    <svg class="shapes" width="380" height="800" viewBox="0 0 380 800" aria-hidden="true">
      <polygon points="0,330 260,290 380,290 380,302 262,304 0,346" fill="var(--coral)"/>
      <polygon points="0,346 262,304 380,302 380,470 0,500" fill="var(--navy)"/>
      <polygon points="0,650 244,650 164,800 0,800" fill="var(--navy)"/>
      <polygon points="246,650 268,650 188,800 166,800" fill="var(--coral)"/>
      <polygon points="212,768 380,768 380,800 195,800" fill="var(--coral)"/>
    </svg>

    <div class="brand-mark"><span>Shuttle Forge</span><span class="dot"></span></div>

    <h1 class="headline">Design for Ladies</h1>
    <p class="subline">Especially for women badminton player</p>

    <div class="product-photo racket" role="img" aria-label="Photo of a badminton racket"></div>
    <div class="product-photo bags" role="img" aria-label="Photo of stacked racket bags"></div>
    <div class="product-photo shoes" role="img" aria-label="Photo of badminton shoes"></div>

    <ul class="brand-list">
      <li>Plume</li><li>KESTRA</li><li>Norvek</li><li>Ru-Pao</li>
    </ul>

    <p class="shipping">We offer shipping to Australia wide and New Zealand wide and <span class="free">free shipping</span> when purchase over <span class="price">$150.00</span></p>

    <div class="promo">
      <div class="promo-rate"><span class="percent">15%</span><span class="label">Off grand<br>opening</span></div>
      <p class="promo-code-label">PROMOCODE</p>
      <p class="promo-code">"Hello18"</p>
      <p class="promo-ends">Ends 2.11.18</p>
    </div>

    <p class="website">www.rallyhaven.com.au</p>
  </article>
</div>
</body>
</html>
```